Super elegant, crisp & clean Business card design required

We recently upgraded our branding - which is on our website - tavorelstudio.com

I would like a simple, yet elegant, clean business card design please.

The font of my logo is Cinzel - and because of the natural colour - it's best to have this on a black background.

I would like to have the back of the business card - with simply my logo.

PLEASE DO NOT SUBMIT A COMPLICATED / UNCLEAN DESIGN

Industry/Entity Type

Business

Contact Information for Business Card

Dalvik Ostrander Photography

Font styles to use
Other font styles liked:
• Cinzel

Requirements
Must have
• A backpage with nothing but my logo
• Simple design - stands out
Should not have
• Colour that dont align with my logo
• Over complicated '/ non symmetrical design

```html
<!DOCTYPE html>
<html lang="en">
<head>
<meta charset="utf-8">
<title>Dalvik Ostrander Photography — Business Card</title>
<link rel="stylesheet" href="https://fonts.googleapis.com/css2?family=Cinzel:wght@400;500&display=swap">
<style>
  :root {
    --backdrop: #2b2724;
    --card-top: #1d1d1d;
    --card-bottom: #080808;
    --gold: #a99a80;
    --gold-soft: #8a7d67;
    --rule: rgba(169, 154, 128, 0.55);
  }
  * { box-sizing: border-box; margin: 0; padding: 0; }
  html, body {
    width: 1200px;
    height: 871px;
    overflow: hidden;
    background: var(--backdrop);
  }
  .stage {
    position: relative;
    width: 1200px;
    height: 871px;
    display: flex;
    justify-content: center;
    align-items: center;
    gap: 80px;
  }
  .card {
    position: relative;
    width: 340px;
    height: 595px;
    background: linear-gradient(180deg, var(--card-top) 0%, var(--card-bottom) 60%);
    border-radius: 3px;
    box-shadow: 0 18px 40px rgba(0, 0, 0, 0.45);
    font-family: "Cinzel", serif;
    color: var(--gold);
    text-align: center;
  }
  .wordmark {
    position: absolute;
    left: 0;
    right: 0;
    display: flex;
    flex-direction: column;
    align-items: center;
  }
  .wordmark__circle {
    width: 58px;
    height: 58px;
    border: 1.5px solid var(--gold);
    border-radius: 50%;
    margin-bottom: 22px;
  }
  .wordmark__name {
    font-size: 24px;
    font-weight: 400;
    letter-spacing: 0.02em;
    line-height: 1;
  }
  .wordmark__tag {
    font-size: 11px;
    letter-spacing: 0.62em;
    margin-top: 6px;
    padding-left: 0.62em;
    color: var(--gold-soft);
  }
  .card--front .wordmark { top: 64px; }
  .card--back .wordmark { top: 235px; }

  .contact {
    position: absolute;
    left: 0;
    right: 0;
    top: 330px;
    display: flex;
    flex-direction: column;
    align-items: center;
  }
  .contact__name {
    font-size: 21px;
    line-height: 1.1;
  }
  .contact__role {
    font-size: 18px;
    line-height: 1.1;
    margin-bottom: 44px;
  }
  .contact__item {
    font-size: 15px;
    letter-spacing: 0.03em;
    padding: 10px 0;
    width: 250px;
  }
  .contact__item + .contact__item {
    border-top: 1px dashed var(--rule);
  }
</style>
</head>
<body>
  <main class="stage">
    <article class="card card--front" aria-label="Business card front">
      <div class="wordmark">
        <span class="wordmark__circle" aria-hidden="true"></span>
        <span class="wordmark__name">Dalvik Ostrander</span>
        <span class="wordmark__tag">PHOTOGRAPHY</span>
      </div>
      <div class="contact">
        <p class="contact__name">Dalvik Ostrander</p>
        <p class="contact__role">Photography</p>
        <p class="contact__item">555-214-7380</p>
        <p class="contact__item">INFO@TAVORELSTUDIO.COM</p>
        <p class="contact__item">WWW.TAVORELSTUDIO.COM</p>
      </div>
    </article>

    <article class="card card--back" aria-label="Business card back">
      <div class="wordmark">
        <span class="wordmark__circle" aria-hidden="true"></span>
        <span class="wordmark__name">Dalvik Ostrander</span>
        <span class="wordmark__tag">PHOTOGRAPHY</span>
      </div>
    </article>
  </main>
</body>
</html>
```